We Buy Houses Website

Looking for a highly motivated and skillfull designer to design and code me a "we Buy Houses" type website. I have a potential logo, but if you think you can make a BETTER one, please do try and incorporate it in your template. I am looking for creativity, professionalism, simple yet elegant. I will need a simple form on the front of the template along with pictures I provide you of recent houses I have bought. Look at these sites for examples of the layout of the website:

http://www.brickwaleholdings.example/
http://www.marlowtakesplots.example/
http://www.quickdwellingexit.example/

If you make me a design that blows me away, and you are dependable, you will become part of my team and in charge of the web aspect which will include designing, updating, any and all graphics and logo work, SEO, coding. If you have skills in all of these areas please make me a design and lets do business!! The name of the website will be "Tovin Takes Homes" at TovinTakesHomes.example

I have uploaded some pictures of houses that we have done, please feel free to incorporate this into the banner or the design, etc. I want them to know we buy houses in ANY condition, as is, cash, can close immediately so they can get on with their life. We have many options to help them find a solution to whatever problem they have. We are in the business of helping people.

Target Market(s)

People looking to sell their houses
people facing foreclosure, bankruptcy, death in the family, divorce, anyone that we can help
people with ugly houses that need a lot of repair

Industry/Entity Type

Business

Font styles to use
Serif
Sans Serif

Colors

Designer to choose colors to be used in the design.

Requirements
Must have
• must have a simple form on the front of the page, preferrably near the banner, with the few required fields to help someone get started putting in their interest to sell their house, view the 2 websites i put as examples to see what kind of fields it should have.

My phone number (555) 481-7720 along with a Tovin Takes Homes logo, clean simple and elegant and professional. I want a nice color scheme that is not white but professional and has a wow factor.

```html
<!DOCTYPE html>
<html lang="en">
<head>
<meta charset="utf-8">
<title>Tovin Takes Homes — Sell Your House Fast, For Cash</title>
<link href="https://fonts.googleapis.com/css2?family=Oswald:wght@500;600&family=Open+Sans:ital,wght@0,400;0,700;0,800;1,800&display=swap" rel="stylesheet">
<style>
:root{
  --navy:#020a1f;
  --navy-2:#0a1229;
  --green:#9acd32;
  --green-dark:#7fae1f;
  --page:#efefef;
  --text:#333;
  --muted:#999;
  --rule:#d6d6d6;
  --nav-top:#6a6d74;
  --nav-bot:#4a4d55;
  --footer-bar:#5a5d64;
  --white:#fff;
}
*{box-sizing:border-box;margin:0;padding:0}
html,body{width:811px;height:1200px;overflow:hidden}
body{position:relative;background:var(--page);font-family:"Open Sans",Arial,sans-serif;color:var(--text);font-size:9px}
.abs{position:absolute}
.heading{font-family:"Oswald",Arial,sans-serif;text-transform:uppercase;color:var(--navy)}

/* header */
.site-header{left:0;top:0;width:811px;height:75px;background:var(--navy)}
.brand{left:115px;top:18px;display:flex;align-items:center;gap:7px;color:var(--green);font-family:"Oswald",sans-serif;font-weight:600;font-size:17px;letter-spacing:.3px}
.brand-mark{width:22px;height:22px;background:var(--green)}
.phone{left:461px;top:13px;color:#c9ccd3;font-size:16px;display:flex;align-items:center;gap:6px}
.social{left:607px;top:13px;display:flex;gap:4px}
.social span{width:18px;height:18px;background:#8b8e94;display:block}
.search{left:535px;top:45px;width:160px;height:18px;background:#5c5f66;border-radius:2px;color:#9da0a6;font-size:8px;padding:3px 7px}
.search svg{position:absolute;right:6px;top:3px}

/* nav */
.main-nav{left:0;top:75px;width:811px;height:29px;background:linear-gradient(var(--nav-top),var(--nav-bot))}
.main-nav a{position:absolute;top:0;height:29px;line-height:29px;color:#e4e5e8;font-size:9px;text-decoration:none;transform:translateX(-50%)}
.main-nav a.active{background:var(--green);color:var(--white);width:62px;text-align:center}

/* hero */
.hero{left:0;top:104px;width:811px;height:319px}
.hero-photo{width:100%;height:100%;background:linear-gradient(180deg,#4d8ad8 0%,#8fb7e8 22%,#a8a196 40%,#6b6155 58%,#4f7a2c 72%,#3c6a1f 100%)}
.hero-copy{left:125px;top:178px;width:310px;color:var(--white)}
.hero-copy h1{font-family:"Oswald",sans-serif;font-weight:500;font-size:25px;line-height:1;margin-bottom:8px}
.hero-copy h2{font-weight:800;font-size:14px;line-height:1.12;margin-bottom:8px}
.hero-copy p{font-size:9px;line-height:1.35}
.lead-form{left:487px;top:136px;width:195px;height:258px;background:rgba(240,240,240,.93);box-shadow:0 0 6px rgba(0,0,0,.4)}
.lead-form h3{background:linear-gradient(#b2de4a,var(--green));height:33px;line-height:33px;text-align:center;font-family:"Oswald",sans-serif;font-weight:500;font-size:16px;color:var(--navy);border-bottom:1px solid var(--green-dark)}
.field{position:absolute;left:14px;width:165px;height:24px;background:var(--white);border:1px solid #ddd;color:#888;font-size:8px;padding:6px 8px}
.submit{position:absolute;left:14px;top:221px;width:78px;height:21px;background:var(--green);color:var(--navy);font-size:8px;text-align:center;line-height:21px}

/* feature strips */
.feature{top:447px;width:186px;height:75px;background:var(--white);border-left:6px solid var(--green);padding:9px 14px;box-shadow:0 1px 3px rgba(0,0,0,.12)}
.feature h4{font-weight:800;font-style:italic;font-size:15px;color:var(--navy);text-transform:uppercase;letter-spacing:-.3px}
.feature h4 em{color:var(--green)}
.feature p{color:#555;font-size:8.5px;line-height:1.3;margin-top:4px}
.rule{height:1px;background:var(--rule)}

/* offers */
.section-title{font-size:17px;font-weight:500}
.offer{top:598px;width:140px}
.offer .thumb{width:140px;height:108px;background:var(--white);padding:5px;box-shadow:0 1px 3px rgba(0,0,0,.2)}
.offer .thumb div{width:100%;height:100%}
.caption-title{font-weight:700;font-size:8.5px;color:#333;text-transform:uppercase;margin-top:7px}
.caption-sub{color:#666;font-size:8.5px;margin-top:2px}
.price{color:var(--green);font-size:8.5px;margin-top:4px}
.more{color:var(--green);font-size:8.5px}

/* welcome & news */
.welcome-photo{left:118px;top:814px;width:215px;height:107px;background:var(--white);padding:5px;box-shadow:0 1px 3px rgba(0,0,0,.2)}
.welcome-photo div{width:100%;height:100%;background:linear-gradient(135deg,#4a2d1c,#8a6a4a 55,#c9b79a)}
.body-copy{color:#888;font-size:8.5px;line-height:1.4}
.news-thumb{left:396px;width:88px;height:70px;background:var(--white);padding:4px;box-shadow:0 1px 3px rgba(0,0,0,.2)}
.news-thumb div{width:100%;height:100%}

/* footer */
.site-footer{left:0;top:1040px;width:811px;height:135px;background:var(--navy-2)}
.footer-col{top:20px;color:#c9ccd3;font-size:8.5px}
.footer-col h5{font-family:"Oswald",sans-serif;font-weight:500;font-size:15px;color:var(--white);margin-bottom:10px}
.footer-col li{list-style:none;margin-bottom:8px;position:relative;padding-left:11px}
.footer-col li::before{content:"";position:absolute;left:0;top:4px;width:3px;height:3px;background:var(--green)}
.footer-col li.current{color:var(--green)}
.contact p{line-height:1.5}
.contact .mail{color:var(--green)}
.footer-bar{left:0;top:1175px;width:811px;height:25px;background:var(--footer-bar);color:#c9ccd3;font-size:8px;padding:8px 115px}
</style>
</head>
<body>

<header class="abs site-header">
  <div class="abs brand"><span class="brand-mark"></span>TOVIN TAKES HOMES</div>
  <div class="abs phone">
    <svg width="14" height="11" viewBox="0 0 14 11"><path d="M1 3c0-2 12-2 12 0v1.5h-3V3.3c-2-.6-4-.6-6 0v1.2H1z M3 5h8l1.5 5h-11z" fill="#c9ccd3"/></svg>
    (555) 481-7720
  </div>
  <div class="abs social" aria-label="Social links"><span></span><span></span><span></span><span></span></div>
  <div class="abs search">Search
    <svg width="11" height="11" viewBox="0 0 11 11"><circle cx="4.5" cy="4.5" r="3.3" fill="none" stroke="#b9bcc2" stroke-width="1.4"/><path d="M7 7l3 3" stroke="#b9bcc2" stroke-width="1.6"/></svg>
  </div>
</header>

<nav class="abs main-nav">
  <a class="active" style="left:146px">Home</a>
  <a style="left:233px">Sell My House Fast</a>
  <a style="left:335px">How It Works</a>
  <a style="left:417px">About Me</a>
  <a style="left:504px">Recent Projects</a>
  <a style="left:587px">Articles</a>
  <a style="left:656px">Investors</a>
</nav>

<section class="abs hero">
  <div class="hero-photo" role="img" aria-label="Photo of a single-storey house with a green front lawn under a blue sky"></div>
</section>
<div class="abs hero-copy">
  <h1>SELL YOUR HOUSE FAST, FOR CASH</h1>
  <h2>FIND A SIMPLER WAY TO SELL YOUR HOME, WITH NO FEES, NO COMMISSIONS IN AS-IS CONDITION.</h2>
  <p>Lorem ipsum dolor sit amet, consectetur adipiscing elit. Etiam placerat neque id malesuada tincidunt. Ut sit amet nibh aliquam, condimentum sapien sit amet, sollicitudin tortor. Sed viverra ligula eget justo lacinia lobortis. Cum sociis natoque penatibus et magnis dis parturient montes, nascetur ridiculus mus. Integer blandit odio eu cursus egestas. Sed urna ante, sollicitudin id scelerisque ac, elementum id ante.</p>
</div>
<form class="abs lead-form">
  <h3>Complete to Begin</h3>
  <div class="field" style="top:45px">First Name</div>
  <div class="field" style="top:79px">Last Name</div>
  <div class="field" style="top:114px">Phone No</div>
  <div class="field" style="top:148px">E-Mail</div>
  <div class="field" style="top:183px">Address</div>
  <div class="submit">Submit</div>
</form>

<div class="abs feature" style="left:115px"><h4><em>SALE</em> EXCLUSIVES</h4><p>Lorem ipsum dolor sit amet, consectetur adipiscing elit. Etiam placerat neque id malesuada tincidunt. Ut sit amet nibh...</p></div>
<div class="abs feature" style="left:311px"><h4><em>ELITE</em> RENTALS</h4><p>Lorem ipsum dolor sit amet, consectetur adipiscing elit. Etiam placerat neque id malesuada tincidunt. Ut sit amet nibh...</p></div>
<div class="abs feature" style="left:507px"><h4><em>FEAT</em>URED</h4><p>Lorem ipsum dolor sit amet, consectetur adipiscing elit. Etiam placerat neque id malesuada tincidunt. Ut sit amet nibh...</p></div>

<div class="abs rule" style="left:115px;top:546px;width:580px"></div>
<div class="abs rule" style="left:115px;top:582px;width:222px;background:#555"></div>
<div class="abs rule" style="left:474px;top:582px;width:221px;background:#555"></div>
<h2 class="abs heading section-title" style="left:344px;top:566px">FEATURED OFFERS</h2>

<div class="abs offer" style="left:115px"><div class="thumb"><div role="img" aria-label="Kitchen with dark wood cabinets" style="background:linear-gradient(135deg,#3b2416,#7a5636 60%,#b59b7a)"></div></div><div class="caption-title">LOREM IPSUM DOLOR</div><div class="caption-sub">Tenerife, Canary Islands</div><div class="price">$1,890</div></div>
<div class="abs offer" style="left:262px"><div class="thumb"><div role="img" aria-label="Kitchen with wood cabinets and tiled floor" style="background:linear-gradient(180deg,#d8cdb8,#7a4a2a 50%,#c49a6e)"></div></div><div class="caption-title">LOREM IPSUM DOLOR</div><div class="caption-sub">Tenerife, Canary Islands</div><div class="price">$1,890</div></div>
<div class="abs offer" style="left:409px"><div class="thumb"><div role="img" aria-label="Empty room with carpet floor" style="background:linear-gradient(180deg,#cfc3a6,#6a5a3e 55%,#b4728a)"></div></div><div class="caption-title">LOREM IPSUM DOLOR</div><div class="caption-sub">Tenerife, Canary Islands</div><div class="price">$1,890</div></div>
<div class="abs offer" style="left:555px"><div class="thumb"><div role="img" aria-label="Open kitchen and dining area" style="background:linear-gradient(180deg,#d9ccb0,#6b4526 55%,#a88762)"></div></div><div class="caption-title">LOREM IPSUM DOLOR</div><div class="caption-sub">Tenerife, Canary Islands</div><div class="price">$1,890</div></div>

<div class="abs rule" style="left:115px;top:767px;width:580px"></div>

<h2 class="abs heading section-title" style="left:115px;top:784px">WELCOME</h2>
<div class="abs welcome-photo"><div role="img" aria-label="Renovated kitchen with wood cabinets and ceiling lights"></div></div>
<div class="abs" style="left:115px;top:930px;width:225px">
  <div class="caption-title" style="margin:0 0 6px">LOREM IPSUM DOLOR</div>
  <p class="body-copy">Lorem ipsum dolor sit amet, consectetur adipiscing elit. Etiam placerat neque id malesuada tincidunt Praesent tellus dui, pulvinar quis mattis vitae, is at feugiat ut erat.</p>
  <div class="more">[ Read More ]</div>
</div>

<div class="abs" style="left:364px;top:790px;width:1px;height:205px;background:var(--rule)"></div>

<h2 class="abs heading section-title" style="left:394px;top:784px">LATEST NEWS</h2>
<div class="abs news-thumb" style="top:816px"><div role="img" aria-label="Bathroom with vanity and toilet" style="background:linear-gradient(135deg,#3d2a1e,#8b7a6a 55%,#d8d2c8)"></div></div>
<div class="abs" style="left:500px;top:815px;width:200px">
  <div class="caption-title" style="margin:0 0 6px">LOREM IPSUM DOLOR</div>
  <p class="body-copy">Lorem ipsum dolor sit amet, consectetur adipiscing elit. Etiam placerat neque id malesuada tincidunt. Ut sit amet nibh aliquam, condimentum...</p>
  <div class="more" style="margin-top:5px">[ Read More ]</div>
</div>
<div class="abs rule" style="left:394px;top:896px;width:301px"></div>
<div class="abs news-thumb" style="top:909px"><div role="img" aria-label="Room with wooden cabinet and doorway" style="background:linear-gradient(135deg,#e0d8c8,#8a5a2e 55%,#d2c6b0)"></div></div>
<div class="abs" style="left:500px;top:909px;width:200px">
  <div class="caption-title" style="margin:0 0 6px">LOREM IPSUM DOLOR</div>
  <p class="body-copy">Lorem ipsum dolor sit amet, consectetur adipiscing elit. Etiam placerat neque id malesuada tincidunt. Ut sit amet nibh aliquam, condimentum...</p>
  <div class="more" style="margin-top:5px">[ Read More ]</div>
</div>

<div class="abs rule" style="left:115px;top:1020px;width:580px"></div>

<footer class="abs site-footer">
  <div class="abs footer-col" style="left:115px"><h5>Company</h5><ul><li class="current">About us</li><li>Services</li><li>Presentation</li><li>Clients</li></ul></div>
  <div class="abs footer-col" style="left:212px"><h5>Properties</h5><ul><li>Commercial</li><li>Residential</li><li>Luxury</li><li>Modren Home</li></ul></div>
  <div class="abs footer-col" style="left:313px"><h5>Related Services</h5><ul><li>Apartments for Rent</li><li>Senior Housing</li><li>Corporate Housing</li><li>Real Estate Search</li></ul></div>
  <div class="abs footer-col" style="left:453px"><h5>My Account</h5><ul><li>Sign In</li><li>View Cart</li><li>Track My Order</li><li>Help</li></ul></div>
  <div class="abs footer-col contact" style="left:561px"><h5>Contact Info</h5>
    <p>4420 Fenwick Lane, Dunmore,<br>D12 77KT</p>
    <p>Phone: (555) 481-7720</p>
    <p>E-mail: <span class="mail">mail@tovintakeshomes.example</span></p>
  </div>
</footer>
<div class="abs footer-bar">Copyright © 2014 TovinTakesHomes.example All Reserved</div>

</body>
</html>
```